Fox Hollow Brewing Company Spring 2024

https://www.foxhollowhub.com/
www.FoxhollowBrewing.com
Spring Menu change for Brewery, focus on menu that is upmarket yet fresh and fun. 11"x18" layout both sides. out brand kit online offers a lot of direction with fonts, colors, and logos. We do two menu changes a year and want to keep that same look once we find a great design.
Target Market(s)
30-60 year old
Industry/Entity Type
Brewery Restaurant
Font styles to use
Other font styles liked:
- See Brand Kit
Colors
00AB8E
00BBA5
67D7C9
C6EFE9
E9F9F6
Requirements
Must have
- Menu engineering
Nice to have
- Stock food photos

```html
<!DOCTYPE html>
<html lang="en">
<head>
<meta charset="utf-8">
<title>Fox Hollow Brewing Co. — Spring Menu</title>
<link href="https://fonts.googleapis.com/css2?family=Lexend:wght@400;500&family=Figtree:wght@400;500&family=Libre+Caslon+Text:wght@400;700&family=Crimson+Text:wght@400&family=Montserrat:wght@700&display=swap" rel="stylesheet">
<style>
  :root{
    --forest:#10302a;
    --gold:#a57b35;
    --cream:#f7f3ee;
    --ivory:#f3ede2;
    --ink:#1e2a26;
  }
  *{margin:0;padding:0;box-sizing:border-box}
  html,body{width:1200px;height:1122px;overflow:hidden;background:#fff}
  body{position:relative;font-family:"Figtree",sans-serif;color:var(--ink)}

  /* ---------- Cover ---------- */
  .cover{position:absolute;left:34px;top:101px;width:561px;height:908px;background:var(--forest);color:var(--ivory)}
  .cover-frame{position:absolute;left:0;top:0}
  .cover-address{position:absolute;top:55px;width:100%;text-align:center;font-family:"Libre Caslon Text",serif;font-size:7.6px;line-height:11px;letter-spacing:.2px}
  .cover-mark{position:absolute;top:370px;width:100%;text-align:center;font-family:"Montserrat",sans-serif;font-weight:700;color:var(--ivory)}
  .cover-mark .name{font-size:40px;letter-spacing:3px;line-height:1}
  .cover-mark .sub{font-size:13px;letter-spacing:6px;margin-top:12px}
  .cover-square{position:absolute;left:268px;top:322px;width:24px;height:24px;background:var(--ivory)}
  .cover-title{position:absolute;top:560px;width:100%;text-align:center;font-family:"Libre Caslon Text",serif;font-weight:700;font-size:42px;letter-spacing:1px}
  .legend{position:absolute;top:768px;left:60px;right:60px;text-align:center;font-family:"Crimson Text",serif;font-size:7.3px;line-height:10.2px;color:var(--gold);text-transform:uppercase}

  /* ---------- Inside ---------- */
  .inside{position:absolute;left:605px;top:101px;width:561px;height:908px;background:var(--cream)}
  .section-title{font-family:"Lexend",sans-serif;font-weight:500;color:var(--gold);text-align:center;font-size:32px;letter-spacing:.5px;line-height:1}

  .dish{display:grid;grid-template-columns:1fr 56px;column-gap:6px}
  .dish-name{font-family:"Lexend",sans-serif;font-size:8.2px;line-height:10px;text-transform:uppercase}
  .dish-price{font-size:6.6px;line-height:10px}
  .dish-desc{grid-column:1/2;font-size:5.3px;line-height:9.9px}

  .photo{position:absolute}

  /* appetizers */
  .appetizers{position:absolute;left:20px;top:19px;width:261px;height:577px;background:var(--forest);color:var(--ivory)}
  .appetizers .section-title{margin-top:19px}
  .appetizers .photo{left:0;top:61px;width:256px;height:142px;background:radial-gradient(ellipse at 50% 55%,#d9a73a 0%,#b27a2c 35%,#3f7a75 62%,#a5483b 85%)}
  .app-list{position:absolute;left:9px;top:213px;width:240px}
  .halffull{font-size:5.3px;text-align:right;padding-right:23px;line-height:8px}
  .app-list .dish{grid-template-columns:1fr 52px}
  .indent{padding-left:13px}
  .addons-box{position:absolute;left:21px;right:22px;top:535px;border-top:1.5px solid var(--gold);padding-top:8px;text-align:center;font-size:6.4px;line-height:10px}
  .addons-box::after{content:"";display:block;margin-top:6px;border-top:1.5px solid var(--gold)}

  /* salads */
  .salads{position:absolute;left:20px;top:605px;width:261px}
  .salads .section-title{font-size:31px}
  .salads .rule{margin-top:5px;border-top:4px solid var(--gold);height:0}
  .salad-list{margin-top:7px;padding-left:5px;width:235px}
  .salad-list .dish{grid-template-columns:1fr 48px}
  .salads-photo{left:20px;top:818px;width:261px;height:90px;background:linear-gradient(120deg,#7eae3e 0%,#c9412f 35%,#2c2a2a 55%,#f1ede2 75%,#8fbf4a 100%)}

  /* burgers */
  .burgers{position:absolute;left:295px;top:29px;width:239px;height:318px;border:1px solid var(--gold);border-bottom:none}
  .burgers .section-title{margin-top:8px;font-size:33px}
  .intro{font-size:6.2px;font-style:italic;text-align:center;line-height:10px;padding:4px 6px 0}
  .burger-list{margin-top:8px;padding-left:13px;width:225px}
  .burger-list .dish{grid-template-columns:1fr 26px}
  .burgers-photo{left:293px;top:347px;width:243px;height:102px;background:linear-gradient(100deg,#2b2b2a 0%,#b7873f 25%,#6a3b22 35%,#3b3a37 55%,#c08a45 75%,#2a2a28 100%)}
  .burger-addons{position:absolute;left:301px;top:456px;width:250px;font-size:6.5px;line-height:10px;color:var(--gold)}

  /* tacos */
  .tacos{position:absolute;left:287px;top:489px;width:254px;height:420px;background:var(--forest);color:var(--ivory)}
  .tacos-frame{position:absolute;left:8px;top:9px;right:8px;bottom:9px;border:1.5px solid var(--gold)}
  .tacos .section-title{margin-top:21px;font-size:33px}
  .tacos .intro{margin:10px 18px 0;border-top:1.5px solid var(--gold);border-bottom:1.5px solid var(--gold);padding:4px 6px 6px}
  .taco-list{margin-top:8px;padding-left:20px;width:220px}
  .taco-list .dish{grid-template-columns:1fr 26px}
</style>
</head>
<body>

<section class="cover">
  <svg class="cover-frame" width="561" height="908" viewBox="0 0 561 908" aria-hidden="true">
    <path d="M53,23 H508 A24,24 0 0 0 532,47 V861 A24,24 0 0 0 508,885 H53 A24,24 0 0 0 29,861 V47 A24,24 0 0 0 53,23 Z" fill="none" stroke="#a57b35" stroke-width="0.9"/>
  </svg>
  <p class="cover-address">318 AVENUE K<br>CEDAR BLUFF, TX 78600</p>
  <div class="cover-square"></div>
  <div class="cover-mark">
    <p class="name">FOX HOLLOW</p>
    <p class="sub">CB &nbsp;BREWING CO. &nbsp;TX</p>
  </div>
  <h1 class="cover-title">MENU</h1>
  <p class="legend">Legend has it<br>
  A century ago, a mysterious creature stalked the outskirts of Cedar Bluff.<br>
  Some say it was half-man, half-fox. Others claim it was just a fox or simply a man.<br>
  Regardless, the allure of the legend endures, and here at Fox Hollow we embrace the<br>
  spirit of this myth. We believe that the most unforgettable stories, whether<br>
  tall tales or rooted in truth, come alive when shared over cold beer and good company</p>
</section>

<section class="inside">

  <div class="appetizers">
    <h2 class="section-title">APPETIZERS</h2>
    <div class="photo" role="img" aria-label="Photo of loaded nachos with cheese, avocado and tomato"></div>
    <div class="app-list">
      <p class="halffull">(HALF/FULL)</p>
      <div class="dish"><p class="dish-name">Chips and...</p></div>
      <div class="indent">
        <div class="dish"><p class="dish-name">The Trio</p><p class="dish-price">$14</p><p class="dish-desc">A half-size serving each of the Fox Hollow Blonde<br>Beer Cheese, Guacamole, and Salsa</p></div>
        <div class="dish"><p class="dish-name">Guacamole (V)</p><p class="dish-price">$6.5 / 11</p></div>
        <div class="dish"><p class="dish-name">Salsa (V)</p><p class="dish-price">$6 / 9.5</p></div>
        <div class="dish"><p class="dish-name">Fox Hollow Blonde Beer Cheese</p><p class="dish-price">$6.5 / 11.5</p></div>
        <div class="dish"><p class="dish-name">Grizzly Queso</p><p class="dish-price">$7 / 11.5</p><p class="dish-desc">Fox Hollow Blonde Beer Cheese topped with guac,<br>pico de gallo, and cotija cheese</p></div>
      </div>
      <div class="dish"><p class="dish-name">Truffle Fries (V)</p><p class="dish-price">$8</p><p class="dish-desc">Truffle salted french fries. Served with truffle aioli, garnished<br>with shredded Asiago</p></div>
      <div class="dish"><p class="dish-name">Truffle Sprouts (V)</p><p class="dish-price">$11.5</p><p class="dish-desc">Fresh fried Brussels sprouts topped with truffle aioli, pecans,<br>and Asiago cheese</p></div>
      <div class="dish"><p class="dish-name">Onion Rings</p><p class="dish-price">$8.5</p><p class="dish-desc">Beer battered onion rings served with house-made Fox sauce</p></div>
      <div class="dish"><p class="dish-name">Texas Poutine</p><p class="dish-price">$10</p><p class="dish-desc">French fries topped with ancho cheddar gravy, chopped brisket,<br>pico de gallo</p></div>
      <div class="dish"><p class="dish-name">Cheese Curds</p><p class="dish-price">$9.5</p><p class="dish-desc">Crispy fried cheesy goodness. Served with a zesty chipotle-lime<br>sauce</p></div>
      <div class="dish"><p class="dish-name">Chicken Wings (6, 12, 18 PCS)</p><p class="dish-price">$10.5 / $16 / $22</p><p class="dish-desc">Chicken wings hand tossed in your choice of sauce. Served with<br>celery and ranch or blue cheese</p></div>
      <div class="dish"><p class="dish-name">Embellished Nachos</p><p class="dish-price">$11.5</p><p class="dish-desc">Corn tortilla chips with Fox Hollow Blonde Beer Cheese, red sauce,<br>Cotija cheese, lettuce, pico de gallo, pickled onions, jalapeños,<br>and sour cream</p></div>
    </div>
    <div class="addons-box">ADD-ONS:<br>Brisket $4 | Pork Belly $3 | Asada $3 | Chicken $3</div>
  </div>

  <div class="salads">
    <h2 class="section-title">SALADS</h2>
    <div class="rule"></div>
    <div class="salad-list">
      <p class="halffull" style="padding-right:10px">(HALF/FULL)</p>
      <div class="dish"><p class="dish-name">Wedge Salad</p><p class="dish-price">$6 / 11</p><p class="dish-desc">Iceberg lettuce with bacon crumbles, tomatoes, blue cheese<br>crumbles, and blue cheese dressing</p></div>
      <div class="dish"><p class="dish-name">The Seasonal One (GF) (V)</p><p class="dish-price">$6 / 11</p><p class="dish-desc">Spring mixed greens, strawberries, goat cheese, red onions,<br>and toasted pecans. Served with honey-balsamic dressing</p></div>
      <div class="dish"><p class="dish-name">The Champ (V)</p><p class="dish-price">$6 / 11</p><p class="dish-desc">Spring mix with tomato, avocado, cucumber, and red onion.<br>Served with jalapeño-cilantro dressing and topped with crisp<br>tortilla strips</p></div>
      <div class="dish"><p class="dish-name">El Oso (GF) (V)</p><p class="dish-price">$6 / 11</p><p class="dish-desc">Romaine lettuce with grilled corn, black beans, tomatoes,<br>red onion, bell peppers, and chipotle-lime dressing.<br>Topped with Cotija cheese</p></div>
    </div>
  </div>
  <div class="photo salads-photo" role="img" aria-label="Photo of a fresh salad with tomatoes, olives and feta"></div>

  <div class="burgers">
    <h2 class="section-title">BURGERS</h2>
    <p class="intro">All half-pound burgers are cooked medium-well and served on<br>a toasted butter brioche bun with a side of fries, lettuce, tomato,<br>onion, and home-made pickles.</p>
    <div class="burger-list">
      <div class="dish"><p class="dish-name">The Classic One</p><p class="dish-price">$12.5</p><p class="dish-desc">8 oz. Oak Ridge Farms patty with lettuce, tomato, onion, and<br>home-made pickles</p></div>
      <div class="dish"><p class="dish-name">Eggsillent Guy</p><p class="dish-price">$15.25</p><p class="dish-desc">Breakfast burger with bacon, cheddar, a fried egg,<br>and Fox sauce</p></div>
      <div class="dish"><p class="dish-name">The Farmer's Cut</p><p class="dish-price">$14.75</p><p class="dish-desc">8 oz. Oak Ridge Farms patty with jack cheese, thick cut bacon,<br>grilled mushrooms, and white truffle aioli</p></div>
      <div class="dish"><p class="dish-name">The Legendary One</p><p class="dish-price">$14.75</p><p class="dish-desc">8 oz. Oak Ridge Farms patty with thick cut bacon, caramelized<br>onions, aged cheddar, and roasted garlic aioli</p></div>
      <div class="dish"><p class="dish-name">The Laredo One</p><p class="dish-price">$15.5</p><p class="dish-desc">Jack Cheese, Pico de gallo, Mashed avocado, pickled jalapenos<br>with chipotle aioli</p></div>
      <div class="dish"><p class="dish-name">The Lubbock</p><p class="dish-price">$15.5</p><p class="dish-desc">Bacon, Cheddar cheese, onion rings, BBQ sauce</p></div>
      <div class="dish"><p class="dish-name">El Dorado</p><p class="dish-price">$16</p><p class="dish-desc">Half-pound burger with pork belly, cheddar cheese, and horseradish<br>mustard aioli</p></div>
      <div class="dish"><p class="dish-name">Royale with Cheese</p><p class="dish-price">$14.5</p><p class="dish-desc">Served on Texas toast with caramelized onions, cheddar cheese, and<br>Monterey Jack Cheese with Fox sauce</p></div>
    </div>
  </div>
  <div class="photo burgers-photo" role="img" aria-label="Photo of two gourmet burgers on a dark surface"></div>
  <p class="burger-addons">Add-Ons: Cheese $1 | Jalapeños $1 | Bacon $2 | Caramelized Onions $1<br>Sub Fries For: Pick any of our salads $2 | Truffle Fries $2</p>

  <div class="tacos">
    <div class="tacos-frame"></div>
    <h2 class="section-title">TACOS</h2>
    <p class="intro">Each dish comes with 2 tacos with your choice of corn or<br>flour tortillas</p>
    <div class="taco-list">
      <div class="dish"><p class="dish-name">Chicken Fajita Tacos</p><p class="dish-price">$9.5</p><p class="dish-desc">Fajita chicken, grilled peppers and onions, pico de gallo,<br>sharp cheddar, shredded lettuce, and sour cream</p></div>
      <div class="dish"><p class="dish-name">Birria</p><p class="dish-price">$11.5</p><p class="dish-desc">Chopped brisket, jack cheese, topped with onion and<br>cilantro, served with consome</p></div>
      <div class="dish"><p class="dish-name">The Fish Taco</p><p class="dish-price">$10.5</p><p class="dish-desc">Fried fish with avocado, lettuce, pico de gallo, cheddar,<br>and scallion aioli</p></div>
      <div class="dish"><p class="dish-name">Carnitas de Cali (GF)</p><p class="dish-price">$10.5</p><p class="dish-desc">Chopped pork carnitas, grilled corn, Cotija cheese, Baja slaw,<br>and chipotle-lime aioli</p></div>
      <div class="dish"><p class="dish-name">Asada</p><p class="dish-price">$11.5</p><p class="dish-desc">Grilled beef served with pico de gallo, Cotija cheese, fresh<br>cilantro, and onions</p></div>
      <div class="dish"><p class="dish-name">Pork Belly Tacos</p><p class="dish-price">$13.5</p><p class="dish-desc">Tender pork belly with a light and tangy slaw, chipotle aioli,<br>and Cotija cheese</p></div>
      <div class="dish"><p class="dish-name">Brussels Tacos (V)</p><p class="dish-price">$9.5</p><p class="dish-desc">Fried brussel sprouts, pickled red onions, Cotija cheese,<br>chipotle aioli, and cilantro</p></div>
      <div class="dish"><p class="dish-name">Little Jumbo</p><p class="dish-price">$12.5</p><p class="dish-desc">Jumbo shrimp, mashed avocado, Baja slaw, mango habanero<br>glaze, and cilantro-lime aioli</p></div>
    </div>
  </div>

</section>

</body>
</html>
```